Home Inspection Postcard Design

Home inspection. Attached is my old postcard. I would like the card to have the same verbage on it - front and back. but I would like the house graphic and the colors to be blues. The only changes to the information is the website address is www.brightoakhps.com. THe PO Box is now 381 rather than 647, and I wanted to add my email address which is brightoakhps@quillmail.net. I would like to keep the $25 off box but add "or a 10% military discount, which ever is greater" or something like that .If you could mock something up for me I would really appreciate it. I would also like a glossy finish on the cards

Home Inspection

```html
<!DOCTYPE html>
<html lang="en">
<head>
<meta charset="utf-8">
<title>Brightoak Home Inspection Services – Postcard Back</title>
<link rel="stylesheet" href="https://fonts.googleapis.com/css2?family=Oswald:wght@600&family=Arimo:wght@400;700&family=Roboto+Condensed:wght@700&display=swap">
<style>
  :root {
    --stage: #121212;
    --card-white: #ffffff;
    --card-fade: #eef0f4;
    --sky-light: #b6e4f8;
    --sky-mid: #5cc3ee;
    --sky-deep: #1b9ad6;
    --navy-stripe: #1c2f5c;
    --banner-blue: #1a78bb;
    --body-ink: #1f2a38;
    --brand-blue: #1c6fa6;
    --accent-orange: #f08a1c;
    --badge-navy: #1b2a6b;
    --badge-red: #8e1b1b;
    --stamp-grey: #e7e8eb;
    --rule-grey: #8a8d93;
  }
  * { box-sizing: border-box; margin: 0; padding: 0; }
  html, body { width: 1200px; height: 1200px; overflow: hidden; background: var(--stage); }

  .postcard {
    position: absolute; left: 96px; top: 229px;
    width: 1008px; height: 780px;
    background: radial-gradient(ellipse at 70% 45%, var(--card-white) 40%, var(--card-fade) 100%);
    overflow: hidden;
    font-family: "Arimo", Arial, sans-serif;
  }
  .postcard__bands { position: absolute; inset: 0; }

  .headline {
    position: absolute; left: 72px; top: 19px;
    font-family: "Oswald", "Arial Narrow", sans-serif;
    font-weight: 600; font-size: 32px; line-height: 60px;
    color: var(--card-white); white-space: nowrap;
  }

  .pitch {
    position: absolute; left: 30px; top: 100px;
    width: 426px; height: 420px;
    font-size: 18px; line-height: 24.2px;
    color: var(--body-ink); text-align: right;
  }
  .pitch__edge {
    float: right; width: 80px; height: 420px;
    shape-outside: polygon(99% 0, 100% 0, 100% 100%, 8% 100%);
  }

  .contact {
    position: absolute; left: 84px; top: 538px;
    list-style: none; font-size: 20px; line-height: 25px;
    color: var(--brand-blue);
  }
  .contact__item { display: flex; align-items: flex-start; gap: 12px; }
  .contact__icon { width: 14px; height: 25px; flex: none; }

  .offer-badge {
    position: absolute; left: 26px; top: 643px;
    width: 118px; height: 118px; border-radius: 50%;
    background: var(--card-white);
    border: 7px solid var(--accent-orange);
    box-shadow: 0 2px 6px rgba(0,0,0,0.25);
    display: flex; flex-direction: column; align-items: center; justify-content: center;
    font-family: "Roboto Condensed", "Arial Narrow", sans-serif; font-weight: 700;
    text-align: center;
  }
  .offer-badge__amount { font-size: 30px; line-height: 30px; color: var(--badge-navy); }
  .offer-badge__note { font-size: 13px; line-height: 14px; color: var(--badge-red); margin-top: 3px; }

  .brand {
    position: absolute; left: 505px; top: 131px; width: 260px;
    text-align: center; color: var(--brand-blue);
  }
  .brand__name { font-size: 45px; line-height: 50px; font-weight: 400; }
  .brand__descriptor { font-size: 12px; line-height: 14px; letter-spacing: 0.3px; }
  .brand__tagline {
    margin-top: 10px;
    font-size: 18px; line-height: 22px;
    color: var(--accent-orange);
  }

  .stamp-box {
    position: absolute; left: 803px; top: 35px;
    width: 170px; height: 170px; background: var(--stamp-grey);
  }

  .address-rule {
    position: absolute; left: 538px; width: 436px;
    height: 1.5px; background: var(--rule-grey);
  }
  .address-rule--1 { top: 428px; }
  .address-rule--2 { top: 520px; }
  .address-rule--3 { top: 610px; }
</style>
</head>
<body>
<main class="postcard">
  <svg class="postcard__bands" width="1008" height="780" viewBox="0 0 1008 780" aria-hidden="true">
    <defs>
      <linearGradient id="panelSky" x1="0" y1="0" x2="1" y2="0.3">
        <stop offset="0" stop-color="var(--sky-light)"/>
        <stop offset="0.6" stop-color="var(--sky-mid)"/>
        <stop offset="1" stop-color="var(--sky-deep)"/>
      </linearGradient>
    </defs>
    <polygon points="0,0 516,0 385,530 385,780 0,780" fill="url(#panelSky)"/>
    <polygon points="470,0 516,0 385,530 360,530" fill="var(--sky-deep)"/>
    <polygon points="508,0 518,0 387,530 377,530" fill="var(--navy-stripe)"/>
    <rect x="62" y="531" width="470" height="228" fill="var(--card-white)"/>
    <polygon points="48,19 473,19 461,79 62,79 48,72" fill="var(--banner-blue)"/>
  </svg>

  <h1 class="headline">Why Do I Need An Inspection?</h1>

  <p class="pitch"><span class="pitch__edge"></span>The purchase of a home or commercial building is one of the largest single investments you will ever make. You should know what to expect — in terms of needed and possible repairs and maintenance. A fresh coat of paint could be hiding serious problems. Stains on the ceiling may indicate a chronic roof leak or may be simply the result of a single incident. The inspector reviews these and other clues, then presents a professional opinion as to the condition of the property to help you avoid unpleasant surprises afterward. Of course, an inspection may also point out the positive aspects of a building, as well as the type of maintenance needed to keep it in proper shape. After the inspection, you will have a much clearer understanding of the property, and be able to make your purchasing decision confidently.</p>

  <ul class="contact">
    <li class="contact__item">
      <svg class="contact__icon" viewBox="0 0 14 25" aria-hidden="true"><path d="M7 5a5 5 0 0 0-5 5c0 3.5 5 9 5 9s5-5.5 5-9a5 5 0 0 0-5-5zm0 7a2 2 0 1 1 0-4 2 2 0 0 1 0 4z" fill="var(--brand-blue)"/></svg>
      <span>P.O. Box 381<br>Fairbrook, GA 31390</span>
    </li>
    <li class="contact__item">
      <svg class="contact__icon" viewBox="0 0 14 25" aria-hidden="true"><rect x="1" y="8" width="12" height="9" fill="var(--brand-blue)"/><path d="M1 8l6 5 6-5" stroke="#fff" stroke-width="1.2" fill="none"/></svg>
      <span>brightoakhps@quillmail.net</span>
    </li>
    <li class="contact__item">
      <svg class="contact__icon" viewBox="0 0 14 25" aria-hidden="true"><g fill="none" stroke="var(--brand-blue)" stroke-width="1.2"><circle cx="7" cy="13" r="6"/><ellipse cx="7" cy="13" rx="2.6" ry="6"/><path d="M1 13h12"/></g></svg>
      <span>www.brightoakhps.com</span>
    </li>
  </ul>

  <div class="offer-badge">
    <span class="offer-badge__amount">$25Off</span>
    <span class="offer-badge__note">10% military<br>discount</span>
  </div>

  <div class="brand">
    <div class="brand__name">Brightoak</div>
    <div class="brand__descriptor">HOME INSPECTION SERVICES LLC.</div>
    <div class="brand__tagline">Every Corner, Every Detail</div>
  </div>

  <div class="stamp-box" aria-label="Postage stamp area"></div>

  <div class="address-rule address-rule--1"></div>
  <div class="address-rule address-rule--2"></div>
  <div class="address-rule address-rule--3"></div>
</main>
</body>
</html>
```